Vela Norvina is a dietary supplement company and in need of label design for 4 products

label for 4 dietary supplement products :1- Biotin. Red bottle ( please see the picture attached, not the whole bottle is colored but rather its a white bottle with the upper part and lower part of the bottle colored)2- COQ10. Orange Bottle 3- Hair Skin Nail. Pink bottle 4- Probiotics. Green Bottle we like the label to:1- have a modern and sleek appearance with very limited graphics.2- have a transparent background( as the bottle is white )3- have the box with the supplement and ingredient to appear sideways( horizontal )4- to have a color matching the bottle color.attached you will find :1- the dimension of the bottle.2- four different labels for each of the products.3- two pictures of the bottles 4- picture of the caps5- Logo
Industry/Entity Type
Health And Wellness
Colors
Designer to choose colors to be used in the design.
Look and feel
Each slider illustrates characteristics of the customer's brand and the style your logo design should communicate.

```html
<!DOCTYPE html>
<html lang="en">
<head>
<meta charset="utf-8">
<title>Vela Norvina CoQ10 Label</title>
<link rel="stylesheet" href="https://fonts.googleapis.com/css2?family=Anton&family=Oswald:wght@400;500;600&family=Lora:wght@400;500&display=swap">
<style>
  :root {
    --orange: #ef6a1e;
    --orange-deep: #e85c17;
    --gold: #f4c98a;
    --ink: #2f3433;
    --slate: #3f4a48;
    --paper: #ffffff;
    --mist: #eef0f0;
    --stage: #f3f3f3;
    --leaf: #4d8b32;
    --blue: #2b87d1;
  }
  * { box-sizing: border-box; margin: 0; padding: 0; }
  html, body { width: 1082px; height: 1200px; overflow: hidden; background: var(--stage); }
  body { position: relative; font-family: "Lora", serif; color: var(--ink); }

  .label {
    position: absolute; left: 21px; top: 387px; width: 1040px; height: 426px;
    background: linear-gradient(180deg, var(--paper) 0%, var(--mist) 100%);
    overflow: hidden;
  }
  .band-top { position: absolute; left: 0; top: 0; width: 100%; height: 32px; background: var(--orange); border-bottom: 2px solid var(--gold); }
  .band-bottom { position: absolute; left: 0; top: 272px; width: 100%; height: 154px; background: linear-gradient(180deg, var(--orange) 0%, var(--orange-deep) 100%); border-top: 2px solid var(--gold); }

  .panel { position: absolute; left: 36px; width: 242px; border: 1.5px solid var(--orange); background: var(--paper); font-size: 8.4px; line-height: 1.28; padding: 12px 10px 4px; color: #4a4a4a; overflow: hidden; }
  .panel-tag { position: absolute; top: -1px; left: 8px; background: var(--orange); color: #fff; font-size: 8px; letter-spacing: .3px; padding: 1px 9px; }
  .suggested { top: 48px; height: 66px; }
  .caution { top: 123px; height: 66px; text-align: justify; font-size: 7.9px; line-height: 1.24; padding: 12px 8px 3px; letter-spacing: -0.1px; }
  .warning { top: 199px; height: 66px; text-align: center; font-size: 9.6px; line-height: 1.3; color: var(--ink); padding-top: 9px; }

  .icons { position: absolute; left: 120px; top: 280px; display: flex; gap: 12px; }
  .fda-note { position: absolute; left: 36px; top: 308px; width: 242px; height: 33px; border: 1px solid #fff; color: #fff; font-size: 7px; line-height: 1.25; text-align: center; padding: 3px 10px; }
  .lot { position: absolute; left: 33px; top: 402px; color: #fff; font-size: 8.6px; }

  .brand { position: absolute; left: 444px; top: 52px; width: 150px; height: 84px; display: flex; align-items: center; justify-content: center; gap: 7px; }
  .brand-name { font-family: "Lora", serif; font-size: 20px; font-weight: 500; color: var(--ink); }
  .brand-dot { width: 9px; height: 9px; background: var(--leaf); }

  .capsules { position: absolute; left: 440px; top: 156px; width: 160px; height: 98px; border-radius: 50%; background: radial-gradient(ellipse at center, var(--blue) 0%, #9fc9ec 55%, rgba(255,255,255,0) 75%); }

  .ribbon { position: absolute; left: 387px; top: 261px; width: 264px; height: 24px; }
  .ribbon-text { position: absolute; inset: 0; display: flex; align-items: center; justify-content: center; font-family: "Oswald", sans-serif; font-weight: 500; font-size: 17px; letter-spacing: 2.6px; color: #fff; }
  .product { position: absolute; left: 0; width: 1040px; text-align: center; color: #fff; }
  .product-name { top: 287px; font-family: "Anton", sans-serif; font-size: 66px; line-height: 76px; letter-spacing: 1px; }
  .product-sub { top: 360px; font-family: "Lora", serif; font-size: 22px; letter-spacing: 1.5px; }
  .category { position: absolute; left: 427px; top: 393px; width: 185px; height: 21px; background: #fff; color: var(--ink); font-family: "Lora", serif; font-size: 12.5px; letter-spacing: 1.6px; text-align: center; line-height: 21px; }

  .facts { position: absolute; left: 758px; top: 51px; width: 248px; height: 174px; border: 1.5px solid var(--orange); background: var(--paper); font-family: "Oswald", sans-serif; color: var(--ink); }
  .facts-title { font-size: 30px; font-weight: 500; color: var(--orange); padding: 0 9px; line-height: 43px; border-bottom: 1px solid var(--orange); margin: 0 2px; }
  .facts-serving { font-size: 11px; padding: 5px 9px 4px; line-height: 15px; }
  .facts-rule { height: 6px; background: var(--orange); margin: 0 3px; }
  .facts-row { display: flex; justify-content: space-between; font-size: 10px; padding: 5px 9px; border-bottom: 1px solid var(--orange); margin: 0 3px; }
  .facts-row.head { justify-content: flex-end; gap: 18px; }
  .facts-row.item { font-size: 11px; padding: 8px 9px; }
  .facts-foot { font-size: 10px; padding: 6px 9px; }
  .inactive { position: absolute; left: 758px; top: 235px; width: 248px; font-size: 8.6px; line-height: 1.25; text-align: center; color: var(--ink); }
  .inactive span { color: var(--orange); }

  .distributor { position: absolute; left: 799px; top: 293px; width: 167px; height: 65px; border: 1px dashed #fff; color: #fff; font-size: 8.4px; line-height: 13px; text-align: center; padding-top: 10px; }
  .distributor-tag { position: absolute; top: -7px; left: 41px; width: 85px; background: #fff; color: var(--orange); border-radius: 8px; font-size: 10px; line-height: 14px; }
  .seals { position: absolute; left: 818px; top: 376px; display: flex; gap: 19px; }
  .seal { width: 30px; height: 30px; border-radius: 50%; background: #e2e4e6; border: 2px solid #9aa0a4; }
</style>
</head>
<body>
  <section class="label">
    <div class="band-top"></div>
    <div class="band-bottom"></div>

    <div class="panel suggested"><span class="panel-tag">SUGGESTED USE</span>As a dietary supplement take one (1) capsule twice a day. For best results take 20-30 min before a meal with an 8oz. glass of water or as directed by your healthcare professional.</div>
    <div class="panel caution"><span class="panel-tag">CAUTION</span>Do not exceed recommended dose. Pregnant or nursing mothers, children under the age of 18, and Individuals with a known medical condition should consult a physician before using this or any dietary supplement.</div>
    <div class="panel warning">KEEP OUT OF REACH OF CHILDREN.<br>DO NOT USE IF SAFETY SEAL IS DAMAGED<br>OR MISSING.<br>STORE IN A COOL, DRY PLACE.</div>

    <div class="icons">
      <svg width="16" height="16" viewBox="0 0 16 16" aria-label="Warning"><path d="M8 1 L15 15 H1 Z" fill="none" stroke="#fff" stroke-width="1.4"/><path d="M8 6 V10 M8 12 V13" stroke="#fff" stroke-width="1.4"/></svg>
      <svg width="16" height="16" viewBox="0 0 16 16" aria-label="Recycle"><circle cx="8" cy="8" r="6" fill="none" stroke="#fff" stroke-width="2" stroke-dasharray="8 4"/></svg>
      <svg width="16" height="16" viewBox="0 0 16 16" aria-label="Dispose properly"><rect x="7" y="6" width="6" height="9" fill="none" stroke="#fff" stroke-width="1.4"/><path d="M6 5 H14" stroke="#fff" stroke-width="1.4"/><circle cx="4" cy="4" r="1.6" fill="#fff"/><path d="M4 6 V11" stroke="#fff" stroke-width="1.6"/></svg>
    </div>
    <div class="fda-note">These statements have not been evaluated by the Food and Drug Administration. This product is not intended to diagnose, treat, cure or prevent any disease.</div>
    <div class="lot">LOT# and Expiration date printed on bottom of Bottle. V2RO</div>

    <div class="brand"><span class="brand-dot"></span><span class="brand-name">Vela Norvina</span></div>
    <div class="capsules" role="img" aria-label="Pile of blue and white capsules"></div>

    <div class="ribbon">
      <svg width="264" height="24" viewBox="0 0 264 24"><polygon points="0,12 12,0 252,0 264,12 252,24 12,24" fill="var(--slate)"/></svg>
      <div class="ribbon-text">PRIVATE LABELING</div>
    </div>
    <div class="product product-name">COQ10</div>
    <div class="product product-sub">(UBIQUINONE)</div>
    <div class="category">DIETARY SUPPLEMENTS</div>

    <div class="facts">
      <div class="facts-title">Supplement Facts</div>
      <div class="facts-serving">Serving Size: 1 Capsules<br>Servings Per Container: Any Count</div>
      <div class="facts-rule"></div>
      <div class="facts-row head"><span>Amount Per Serving</span><span>%DV</span></div>
      <div class="facts-row item"><span>Coenzyme Q-10 (Ubiquinone) &nbsp;&nbsp;1500mg</span><span>**</span></div>
      <div class="facts-foot">** Daily Value (DV) not established</div>
    </div>
    <div class="inactive"><span>Inactive Ingredients:</span> Cellulose (Vegetable Capsule),<br>Rice Bran.</div>

    <div class="distributor"><div class="distributor-tag">Distributed By:</div>Company Name<br>Street Address<br>City, ST Zipcode<br>Website or Phone Number</div>
    <div class="seals"><span class="seal"></span><span class="seal"></span><span class="seal"></span></div>
  </section>
</body>
</html>
```